Vision / Mission Poster Required

We are looking to display our company Vision / Mission / Values on a poster. This will be displayed in the head office and other site offices.

The document needs to look professional however still be fun, eye catching and easy to read. It will be predominantly displayed in A3 format.

The design needs to use our company Logo which is attached along with the Text to display on the poster. I have put some additional text on the doc that you can include if it suits the layout but is not essential.

Target Market(s)

Staff, Corporate Visitors

Industry/Entity Type

Electric Company

Font styles to use
Sans Serif

Colors

Designer to choose colors to be used in the design.

Requirements
Must have
• Incorporate Logo
• Professional Look
• Attention grabbing
• Easy to Read
Should not have
• Lightning Bolts
• Pictures of random people/Things

```html
<!DOCTYPE html>
<html lang="en">
<head>
<meta charset="utf-8">
<title>Clearpath Electrical – Vision, Mission and Values</title>
<link rel="stylesheet" href="https://fonts.googleapis.com/css2?family=Montserrat:wght@800&family=Lato:ital,wght@0,400;0,700;1,400&display=swap">
<style>
  :root{
    --navy:#1d3b78;
    --navy-dark:#15305f;
    --orange:#f07622;
    --sky:#d3e3f1;
    --panel:#e9eaec;
    --ink:#2b2b2b;
    --white:#ffffff;
  }
  *{box-sizing:border-box;margin:0;padding:0}
  html,body{width:801px;height:1200px;overflow:hidden;background:#fff}
  .poster{position:relative;width:801px;height:1200px;background:var(--white);font-family:"Lato",sans-serif;color:var(--ink)}
  .top-band{position:absolute;left:0;top:0;width:801px;height:45px;background:var(--sky)}
  .hero-photo{position:absolute;left:0;top:0}
  .headline{position:absolute;left:10px;top:66px;width:460px;text-align:center;font-family:"Montserrat",sans-serif;font-weight:800;font-size:36px;line-height:47px;color:var(--navy)}
  .tagline{position:absolute;left:0;top:225px;width:520px;height:32px;}
  .tagline span{position:absolute;left:43px;top:3px;font-style:italic;font-size:23px;color:var(--white);letter-spacing:.3px}
  .goal{position:absolute;top:285px;width:240px}
  .goal-ribbon{position:absolute;left:0;top:0}
  .goal-title{position:absolute;left:0;top:18px;width:240px;text-align:center;color:var(--white);font-size:15px;font-weight:700}
  .goal-body{position:absolute;left:19px;top:60px;width:200px;height:165px;background:var(--panel);border-radius:0 0 16px 16px;padding:22px 12px 0;text-align:center;font-size:15px;line-height:19.5px;color:#333}
  .values-title{position:absolute;left:23px;top:541px;font-size:21px;font-weight:700;color:var(--navy)}
  .values-rule{position:absolute;left:23px;top:567px;width:340px;height:2px;background:var(--navy)}
  .values-list{position:absolute;left:23px;top:578px;width:345px;font-size:10.8px;line-height:14.2px;color:#333}
  .values-list dt{color:var(--orange);font-size:12.5px;line-height:15px}
  .photo{position:absolute;border:3px solid var(--orange)}
  .banner-photo{position:absolute;left:19px;top:864px}
  .brand-panel{position:absolute;left:470px;top:858px}
  .brand{position:absolute;left:510px;top:905px;display:flex;align-items:center;gap:10px}
  .brand-dot{width:32px;height:32px;border-radius:50%;background:var(--orange)}
  .brand-name{font-size:24px;font-weight:700;color:var(--white);letter-spacing:.5px}
  .footer{position:absolute;left:0;top:1108px}
  .footer-text{position:absolute;left:40px;top:1125px;width:721px;text-align:center;color:var(--white);font-size:8.6px;line-height:11.6px}
</style>
</head>
<body>
<main class="poster">
  <div class="top-band"></div>

  <svg class="hero-photo" width="801" height="260" viewBox="0 0 801 260">
    <defs>
      <linearGradient id="solar" x1="0" y1="0" x2="0.6" y2="1">
        <stop offset="0" stop-color="#8fb0d8"/>
        <stop offset="0.5" stop-color="#3b5c9c"/>
        <stop offset="1" stop-color="#1c2f66"/>
      </linearGradient>
    </defs>
    <path d="M436 0 C480 40 500 150 560 230 C575 245 590 247 610 247 L801 247 L801 0 Z" fill="var(--orange)"/>
    <path role="img" aria-label="Photo of rows of solar panels under a clear sky" d="M446 0 C490 40 512 150 570 228 C582 240 595 241 612 241 L801 241 L801 0 Z" fill="url(#solar)"/>
  </svg>

  <h1 class="headline">To Be Perth’s Premier Provider Of Electrical Service Solutions</h1>

  <svg class="tagline" width="520" height="32" viewBox="0 0 520 32">
    <path d="M0 0 L490 0 L512 32 L0 32 Z" fill="var(--orange)"/>
  </svg>
  <div class="tagline"><span>Dynamic results- Proven reputation</span></div>

  <section class="goal" style="left:27px">
    <div class="goal-body">By:- Maintaining a market presence - Leveraging our technical resources – Networking and developing stakeholder relationships</div>
    <svg class="goal-ribbon" width="240" height="64" viewBox="0 0 240 64"><path d="M0 10 L42 0 L44 8 L240 14 L232 60 L20 62 L18 56 L8 56 Z" fill="var(--navy)"/></svg>
    <div class="goal-title">1: Deliver Growth and Value</div>
  </section>

  <section class="goal" style="left:280px">
    <div class="goal-body" style="padding-top:38px">By:- Increasing revenue – Optimizing capacity utilization – Maintaining expenses</div>
    <svg class="goal-ribbon" width="240" height="64" viewBox="0 0 240 64"><path d="M0 10 L42 0 L44 8 L240 14 L232 60 L20 62 L18 56 L8 56 Z" fill="var(--navy)"/></svg>
    <div class="goal-title" style="top:20px">2: Remain Profitable</div>
  </section>

  <section class="goal" style="left:532px">
    <div class="goal-body">By: - Improving internal efficiency – Diversifying our income sources – Implementing Social &amp; Environmental improvement initiatives</div>
    <svg class="goal-ribbon" width="240" height="64" viewBox="0 0 240 64"><path d="M0 10 L42 0 L44 8 L240 14 L232 60 L20 62 L18 56 L8 56 Z" fill="var(--navy)"/></svg>
    <div class="goal-title" style="top:20px">3: Be Sustainable</div>
  </section>

  <h2 class="values-title">VALUES:</h2>
  <div class="values-rule"></div>
  <dl class="values-list">
    <dt>Honesty &amp;Integrity:</dt>
    <dd>Customers, contractors and suppliers will be able to count on Clearpath personnel to deal straightforwardly and adhere to the strictest moral and ethical codes of conduct.</dd>
    <dt>Safety&amp;Responsibility:</dt>
    <dd>Clearpath is committed to constantly improving safety practices at project job sites and within the electrical service industry as a whole.</dd>
    <dt>Commitment to Quality:</dt>
    <dd>Customers and stakeholders will be able to count on Clearpath workmanship being among the best in the industry.</dd>
    <dt>Innovation &amp; Technology:</dt>
    <dd>Customers can rely on us to apply the latest proven technologies on their projects, and to be on the ground floor of industry standards for new and emerging markets.</dd>
    <dt>Knowledgeable&amp; Valued Employees:</dt>
    <dd>Clearpath recognizes that its greatest asset is its people. We pledge to treat each employee with integrity, dealing honestly with all.</dd>
  </dl>

  <div class="photo" role="img" aria-label="Photo of an electrician in hi-vis working inside a green switch cabinet" style="left:395px;top:541px;width:188px;height:141px;background:linear-gradient(135deg,#2f4a3a,#8a8f70 55%,#d9c64a)"></div>
  <div class="photo" role="img" aria-label="Photo of orange electrical switchboard panels" style="left:594px;top:541px;width:188px;height:141px;background:linear-gradient(135deg,#4a4f58,#e06a1c 55%,#f39a4c)"></div>
  <div class="photo" role="img" aria-label="Photo of a hand using a tablet on site" style="left:395px;top:695px;width:188px;height:141px;background:linear-gradient(135deg,#1f4a66,#c9d2d6 55%,#6a5a4a)"></div>
  <div class="photo" role="img" aria-label="Photo of two electricians in hard hats inspecting a control panel" style="left:594px;top:695px;width:188px;height:141px;background:linear-gradient(135deg,#3a4a3a,#cfd05a 55%,#e8e06a)"></div>

  <svg class="banner-photo" width="766" height="240" viewBox="0 0 766 240">
    <defs>
      <linearGradient id="venue" x1="0" y1="0" x2="1" y2="0">
        <stop offset="0" stop-color="#3a2a12"/>
        <stop offset="0.3" stop-color="#d8b020"/>
        <stop offset="0.55" stop-color="#3a3a40"/>
        <stop offset="0.8" stop-color="#e0a030"/>
        <stop offset="1" stop-color="#c25040"/>
      </linearGradient>
    </defs>
    <path d="M8 2 L110 24 L766 12 L752 236 L0 226 Z" fill="#cfd2d6"/>
    <path role="img" aria-label="Photo of a lively venue interior with hexagonal yellow ceiling lights and a colourful mural" d="M8 0 L110 20 L760 10 L748 228 L0 220 Z" fill="url(#venue)"/>
  </svg>

  <svg class="brand-panel" width="300" height="140" viewBox="0 0 300 140">
    <path d="M6 0 L284 16 L276 132 L0 124 Z" fill="var(--navy)"/>
  </svg>
  <div class="brand"><span class="brand-dot"></span><span class="brand-name">CLEARPATH ELECTRICAL</span></div>

  <svg class="footer" width="801" height="92" viewBox="0 0 801 92">
    <path d="M0 14 Q400 -6 801 14 L801 92 L0 92 Z" fill="var(--navy)"/>
  </svg>
  <p class="footer-text">Serving utilities, builders, large private and commercial clients Clearpath Electrical<br>
  is committed to leading the industry in safety, training and customer satisfaction. We will meet and exceed expectations through our full-spectrum<br>
  of electrical design, build and maintenance services, state-of-the-art assets and financial strength.<br>
  We will continue to embrace new technologies as they emerge and will pursue new and emerging markets. We will maintain our business beliefs and<br>
  pursue unique and challenging projects to help build a culture that nurtures innovative thinking and strategic planning.</p>
</main>
</body>
</html>
```